Mini Book (4.25 x 6) Cover Design for Christian authors

We need a book cover designed for a mini book (4.25 x 6). We will need a front, back and spine for the book.
The book is titled:
Harbor Lanterns
Subtitle:
Quiet Purpose in Every Calling
Authors:
Walter and Renata Oskarsby
We are wanting the colors Dark Blue and Grey with more blue than grey.
We do not want any stock images or photos, only original work.
The cover should convey sincerity, intuition and truth with prestige.
We want the back cover text to be included (top) and the bios to be on the back as well (bottom). *Those documents are included in the files.
Since it is a mini book, it is important for the design to be simple and not cluttered, but powerful!
This is the first book in a twelve book series, so we would like the same "look" to carry through all twelve books, eventually.
On the back of the book, at the bottom (left), we want the following contact information:
Bright Meadow Method Logo (in files below)
tallwillowstudio@mailfernly.com
303.512.4086
P.O.Box 718
Larkhaven, NV 80417

Please save room on the back (bottom-right) for the ISBN and price.
Updates

Thank you to the designers that have submitted feedback concerning our design brief. We have made some changes that will perhaps make it easier to submit a variety of designs.Thank you! Added Saturday, March 4, 2017

Target Market(s)

Christians - mainly women

Industry/Entity Type

Religious

Font styles to use
Serif
Sans Serif
Decorative
Script
Other font styles liked:
• Not any particular font, looking for one that goes well with the cover design.

Requirements
Must have
• Mini Book Size (4.25 x 6)-spine size 1/8" (0.125)
• Dark blue and grey colors
• Cover needs to be simple and not cluttered or busy.
• Intriguing
• A font that is attractive, but it is still easy to read.
• *File information below
Nice to have
• Designs that are different from the mainstream.
• Perhaps a design that would do something different with the title/font? Maybe a repeat of the words from smaller to larger? Not sure how it would look, but maybe?
Should not have
• Any other colors but dark blue and grey
• Cluttered Look

```html
<!DOCTYPE html>
<html lang="en">
<head>
<meta charset="utf-8">
<title>Harbor Lanterns – Cover Spread</title>
<link rel="stylesheet" href="https://fonts.googleapis.com/css2?family=Cinzel:wght@400;600&family=Arimo:wght@400;700&display=swap">
<style>
  :root {
    --blue-deep: #0e3687;
    --blue-main: #1b4ea6;
    --blue-light: #5f93df;
    --blue-glow: #9cc0f0;
    --spine-blue: #163f92;
    --grey-title: #b9bcc1;
    --grey-band: #8d9095;
    --grey-stripe: #c9cbce;
    --text-light: #e6e9ef;
    --text-soft: #c6d0e2;
    --navy-ink: #143a85;
    --page-bg: #ffffff;
  }
  * { box-sizing: border-box; margin: 0; padding: 0; }
  html, body { width: 1200px; height: 1000px; overflow: hidden; background: var(--page-bg); }

  .spread {
    position: absolute; left: 18px; top: 110px;
    width: 1164px; height: 780px;
    display: flex;
    box-shadow: 0 18px 40px rgba(0,0,0,0.12);
  }
  .panel { position: relative; height: 100%; overflow: hidden; }
  .back-cover, .front-cover {
    width: 552px;
    background: linear-gradient(180deg, var(--blue-main) 0%, var(--blue-deep) 100%);
  }
  .spine { width: 60px; background: linear-gradient(90deg, var(--blue-deep), var(--spine-blue) 50%, var(--blue-deep)); }

  .base-band {
    position: absolute; left: 0; right: 0; bottom: 0; height: 92px;
    background: var(--grey-band);
    border-top: 8px solid var(--grey-stripe);
  }

  /* Back cover */
  .back-copy {
    position: absolute; left: 56px; top: 56px; width: 446px;
    font-family: "Arimo", Arial, sans-serif; font-size: 14.5px; line-height: 1.32;
    color: var(--text-soft); text-align: justify;
  }
  .back-copy h2 { font-size: 15px; font-weight: 700; color: var(--text-light); }
  .back-copy p { margin-bottom: 16px; }
  .back-copy ul { list-style: none; margin-bottom: 16px; text-align: left; }
  .back-copy li::before { content: "• "; }
  .back-copy .lead { margin-bottom: 0; }
  .verse { text-align: left; }
  .contact { text-align: left; line-height: 1.3; }
  .method-mark {
    display: flex; align-items: center; gap: 8px; margin-top: 14px;
    font-family: "Arimo", Arial, sans-serif; font-size: 12px; color: var(--text-light);
  }
  .method-mark .dot { width: 30px; height: 30px; border-radius: 50%; background: var(--blue-light); flex: none; }
  .isbn, .price {
    position: absolute; bottom: 112px;
    font-family: "Arimo", Arial, sans-serif; font-size: 13px; color: var(--text-soft);
  }
  .isbn { left: 220px; }
  .price { right: 56px; }

  /* Spine */
  .spine-text {
    position: absolute; left: 50%; top: 30px;
    transform: translateX(-50%);
    writing-mode: vertical-rl;
    display: flex; align-items: center; gap: 28px;
    font-family: "Cinzel", Georgia, serif; color: var(--grey-title);
  }
  .spine-title { font-size: 30px; letter-spacing: 1px; }
  .spine-authors { font-size: 11px; letter-spacing: 2px; text-transform: uppercase; }

  /* Front cover */
  .front-title {
    position: absolute; top: 58px; left: 0; right: 0; text-align: center;
    font-family: "Cinzel", Georgia, serif; font-weight: 400; font-size: 46px;
    color: var(--grey-title); letter-spacing: 1px;
    text-shadow: 0 2px 3px rgba(0,0,0,0.35);
  }
  .cover-art {
    position: absolute; left: 20px; right: 10px; top: 140px; height: 540px;
    background: radial-gradient(ellipse closest-side at 48% 42%, var(--blue-glow) 0%, var(--blue-light) 35%, rgba(27,78,166,0) 100%);
  }
  .subtitle {
    position: absolute; left: 0; right: 0; top: 322px; text-align: center;
    font-family: "Cinzel", Georgia, serif; font-size: 13px; letter-spacing: 2.5px;
    color: var(--navy-ink); text-transform: uppercase;
  }
  .front-authors {
    position: absolute; left: 0; right: 0; bottom: 34px; text-align: center;
    font-family: "Cinzel", Georgia, serif; font-size: 14px; letter-spacing: 2.5px;
    color: var(--text-light); text-transform: uppercase;
  }
</style>
</head>
<body>
<main class="spread">
  <section class="panel back-cover">
    <div class="back-copy">
      <h2>About the book</h2>
      <p>Bright Meadow Method (BMM)® proceeds, prepares and propels us into our Divine Inheritance. God always has our best interest at heart. By understanding His power, we are able to significantly impact the lives of others, leaving our imprint upon their hearts.</p>
      <p class="lead">This book will:</p>
      <ul>
        <li>Uncover the secret that is God's plan</li>
        <li>Unveil God's Six Significant Shields</li>
        <li>Unmask God's Positioning Strategy (GPS)</li>
      </ul>
      <h2>About the author</h2>
      <p>International award winning authors, Renata and Walter Oskarsby inspire couples and individuals to connect to the heart of God through Bright Meadow Method®. For over twenty years, they have conducted workshops and seminars throughout the country and at their private retreat center located in the mountains.</p>
      <p class="verse">"Come, let us go up to the mountain of the LORD,<br>To the house (temple) of the God of Jacob;<br>That He may teach us His ways<br>And that we may walk in His paths." ~ Isaiah 2:3</p>
      <div class="contact">
        tallwillowstudio@mailfernly.com<br>
        303.512.4086<br>
        P.O.Box 718<br>
        Larkhaven, NV 80417
      </div>
      <div class="method-mark"><span class="dot"></span>Bright Meadow Method</div>
    </div>
    <span class="isbn">ISBN</span>
    <span class="price">price.</span>
    <div class="base-band"></div>
  </section>

  <section class="panel spine">
    <div class="spine-text">
      <span class="spine-title">Harbor Lanterns</span>
      <span class="spine-authors">Walter and Renata Oskarsby</span>
    </div>
    <div class="base-band"></div>
  </section>

  <section class="panel front-cover">
    <h1 class="front-title">Harbor Lanterns</h1>
    <div class="cover-art" role="img" aria-label="Illustration of a large grey stone cross in a soft blue glow, with evergreen trees on a grassy knoll at its lower right"></div>
    <p class="subtitle">Quiet Purpose in Every Calling</p>
    <div class="base-band"></div>
    <p class="front-authors">Walter and Renata Oskarsby</p>
  </section>
</main>
</body>
</html>
```